Super Creative! Copper Lantern Ad

CREATIVE CREATIVE CREATIVE needed for our Ad that will be placed on Google Ads, in print and on billboards. Our website is https://mycopperlantern.example

Target Market(s)

B2B

Requirements
Must have
• Uniqueness, creative and the following marks and copy:
1. our logo
2. Our phone number: (555) 274-8830
3. Our website address: mycopperlantern.example
4. Main message: BUILD BRAND. SUSTAIN GROWTH CURVE.

```html
<!DOCTYPE html>
<html lang="en">
<head>
<meta charset="utf-8">
<title>Copper Lantern Ad</title>
<link rel="stylesheet" href="https://fonts.googleapis.com/css2?family=Barlow:ital,wght@0,500;0,600;0,800;1,800;1,900&display=swap">
<style>
  :root {
    --page: #ffffff;
    --sky: #7ae4f4;
    --band-start: #4cbdef;
    --band-end: #1584dc;
    --navy: #0f1d4e;
    --navy-deep: #14185a;
    --blue-start: #1b9ae6;
    --blue-end: #1260b8;
    --orange: #f7931e;
    --white: #ffffff;
    --shadow: rgba(10, 40, 90, 0.35);
  }
  * { margin: 0; padding: 0; box-sizing: border-box; }
  html, body { width: 1200px; height: 1200px; overflow: hidden; background: var(--page); }
  body { position: relative; font-family: "Barlow", sans-serif; }

  .ad {
    position: absolute; left: 200px; top: 335px; width: 800px; height: 530px;
    background: var(--sky); overflow: hidden;
  }
  .ad__band {
    position: absolute; left: 0; right: 0; top: 408px; bottom: 0;
    background: linear-gradient(90deg, var(--band-start), var(--band-end));
  }
  .brand {
    position: absolute; right: 26px; top: 24px;
    display: flex; align-items: center; gap: 7px;
    font-weight: 600; font-size: 19px; letter-spacing: 0.3px; color: var(--navy);
    text-transform: uppercase;
  }
  .brand__mark { width: 20px; height: 20px; background: var(--navy); }

  .hero-photo { position: absolute; left: 40px; top: 93px; width: 245px; height: 427px; }

  .headline {
    position: absolute; right: 63px; top: 0; width: 620px; height: 380px;
    font-style: italic; font-weight: 900; text-transform: uppercase;
    line-height: 1; color: var(--navy-deep);
  }
  .headline > span {
    position: absolute; right: 0; white-space: nowrap;
    text-shadow: 3px 3px 0 rgba(20, 60, 140, 0.35);
  }
  .headline .accent {
    background: linear-gradient(90deg, var(--blue-start), var(--blue-end));
    -webkit-background-clip: text; background-clip: text; color: transparent;
    text-shadow: none; filter: drop-shadow(3px 3px 0 rgba(20, 60, 140, 0.3));
  }
  .headline .line-1 { top: 31px; font-size: 70px; }
  .headline .line-1 .accent { font-size: 104px; margin-right: 20px; }
  .headline .line-2 { top: 122px; font-size: 105px; }
  .headline .line-3 { top: 225px; font-size: 69px; }
  .headline .line-4 { top: 291px; font-size: 69px; }

  .web-pill {
    position: absolute; left: 405px; top: 383px; width: 362px; height: 50px;
    border-radius: 25px; background: var(--orange);
    box-shadow: 3px 4px 0 var(--shadow);
    display: flex; align-items: center; justify-content: center; gap: 8px;
    color: var(--white); font-weight: 600; font-size: 24px;
  }
  .web-pill svg { width: 20px; height: 16px; }

  .phone-line {
    position: absolute; left: 314px; top: 453px;
    display: flex; align-items: center; gap: 14px;
    color: var(--navy-deep); font-weight: 800; font-size: 56px; line-height: 1;
    letter-spacing: -1px;
  }
  .phone-line svg { width: 40px; height: 40px; }
</style>
</head>
<body>
  <section class="ad" aria-label="Copper Lantern advertisement">
    <div class="ad__band"></div>

    <div class="brand"><span class="brand__mark"></span>Copper Lantern</div>

    <svg class="hero-photo" viewBox="0 0 245 427" role="img" aria-label="Photo of a cheerful young woman with a backpack calling out from a smartphone screen">
      <defs>
        <linearGradient id="photoTone" x1="0" y1="0" x2="1" y2="1">
          <stop offset="0" stop-color="#c9a77f"/>
          <stop offset="0.5" stop-color="#6f8fb2"/>
          <stop offset="1" stop-color="#2d3b55"/>
        </linearGradient>
      </defs>
      <rect x="0" y="0" width="245" height="427" rx="24" fill="url(#photoTone)"/>
    </svg>

    <h1 class="headline">
      <span class="line-1"><span class="accent">Build</span>Brand</span>
      <span class="line-2 accent">Sustain</span>
      <span class="line-3">Growth</span>
      <span class="line-4">Curve</span>
    </h1>

    <div class="web-pill">
      <svg viewBox="0 0 22 18" aria-hidden="true"><path d="M2 2l7 7-7 7M11 2l7 7-7 7" fill="none" stroke="#ffd08a" stroke-width="3"/></svg>
      mycopperlantern.example
    </div>

    <div class="phone-line">
      <svg viewBox="0 0 24 24" aria-hidden="true"><path fill="#14185a" d="M6.6 10.8a15.1 15.1 0 0 0 6.6 6.6l2.2-2.2c.3-.3.7-.4 1-.2 1.1.4 2.3.6 3.6.6.6 0 1 .4 1 1V20c0 .6-.4 1-1 1A17 17 0 0 1 3 4c0-.6.4-1 1-1h3.5c.6 0 1 .4 1 1 0 1.3.2 2.5.6 3.6.1.3 0 .7-.2 1z"/></svg>
      (555) 274-8830
    </div>
  </section>
</body>
</html>
```